need professional, precise design for a website

I will start with a homepage design and if we pick your design, we'll have you design up to 6 more interior pages (we'll pay extra for these of course). We need a homepage design for a reserve study company based in Idaho, covering the northwest region. The company is called copper ridge reserve study. Their current site is at https://www.copperridgereserves.example/ and they really like this site for inspiration https://www.fundplannerhub.example/ but they would like an original design, just more modern and fresh like the sample site. I have logo files I will attach. They want something that looks financial and has a feel of accuity. Their main call to action will be to have someone fill in a contact form or call them on the phone. They will have a sample study that someone can download as on the fundplannerhub site. You can use copy from their current site.

```html
<!DOCTYPE html>
<html lang="en">
<head>
<meta charset="utf-8">
<title>Copper Ridge Reserves — Your Financial Road Map</title>
<link rel="stylesheet" href="https://fonts.googleapis.com/css2?family=Cinzel:wght@400;700&family=Libre+Baskerville:ital,wght@0,700;1,700&family=Open+Sans:wght@400;600;700&display=swap">
<style>
:root{
  --navy:#24215f;
  --navy-deep:#1b1a4c;
  --ink:#333338;
  --muted:#6b6b70;
  --rule:#9a9a9a;
  --wash:#f3f3f3;
  --field:#ffffff;
  --footer:#7d7d7f;
  --footer-bar:#6b6b6d;
  --white:#ffffff;
}
*{box-sizing:border-box;margin:0;padding:0}
html,body{width:1200px;height:4615px;overflow:hidden}
body{position:relative;background:var(--white);font-family:"Open Sans",Arial,sans-serif;color:var(--ink)}
.section{position:absolute;left:0;width:1200px}
.rule-v{position:absolute;left:599px;width:1px;background:var(--rule)}
.section-title{position:absolute;left:0;width:1200px;text-align:center;font-family:"Cinzel",Georgia,serif;font-size:40px;letter-spacing:3px;color:var(--navy);font-weight:400}
.btn-outline{display:inline-flex;align-items:center;justify-content:center;gap:6px;width:130px;height:30px;border:1px solid #b5b5b5;border-radius:15px;font-size:10px;font-weight:600;letter-spacing:1px;color:var(--ink);background:var(--white)}
.tri{width:0;height:0;border-left:6px solid currentColor;border-top:4px solid transparent;border-bottom:4px solid transparent}

/* header */
.site-header{top:0;height:75px;background:var(--white)}
.brand{position:absolute;left:125px;top:14px;display:flex;align-items:center;gap:10px}
.brand-dot{width:34px;height:34px;border-radius:50%;background:var(--navy)}
.brand-name{font-family:"Cinzel",Georgia,serif;font-size:21px;color:var(--navy);font-weight:400}
.header-phone{position:absolute;right:100px;top:10px;display:flex;align-items:center;gap:8px;font-size:16px;font-weight:700;color:var(--navy)}
.phone-badge{width:22px;height:22px;border-radius:50%;background:var(--navy);display:flex;align-items:center;justify-content:center}
.main-nav{position:absolute;right:100px;top:46px;display:flex;gap:32px;font-size:12px;letter-spacing:.5px;color:var(--muted)}
.main-nav .active{color:var(--navy);font-weight:600;border-bottom:2px solid var(--navy);padding-bottom:4px}

/* hero */
.hero{top:75px;height:585px;background:linear-gradient(180deg,#3b3f45 0%,#6b6058 38%,#8a7563 52%,#4a4038 72%,#2b2622 100%)}
.hero-copy{position:absolute;top:210px;left:0;width:1200px;text-align:center;color:var(--white)}
.hero-title{font-family:"Cinzel",Georgia,serif;font-weight:700;font-size:54px;letter-spacing:1px;line-height:1}
.hero-sub{font-family:"Libre Baskerville",Georgia,serif;font-weight:700;font-size:36px;margin-top:14px}
.hero-actions{margin-top:26px;display:flex;justify-content:center;gap:8px}
.hero-btn{display:inline-flex;align-items:center;justify-content:center;gap:8px;width:172px;height:42px;font-size:11px;font-weight:700;letter-spacing:1px;color:var(--white)}
.hero-btn.secondary{background:#8d8d8d}
.hero-btn.primary{background:var(--navy)}

/* services */
.services{top:660px;height:725px}
.service{position:absolute;top:190px;width:320px;text-align:center}
.service-icon{width:150px;height:150px;margin:0 auto;display:block}
.service-name{margin-top:22px;font-size:15px;font-weight:700;color:var(--ink)}
.service-text{margin-top:8px;font-size:12.5px;line-height:18px;color:var(--ink);height:145px}
.service .btn-outline{margin-top:10px}

/* about */
.about{top:1385px;height:585px;background:var(--wash)}
.about-video{position:absolute;left:114px;top:215px;width:471px;height:270px;background:radial-gradient(ellipse at 55% 45%,#1c1e28 0%,#0a0a0f 70%)}
.play{position:absolute;left:210px;top:110px;width:52px;height:52px}
.about-text{position:absolute;left:620px;top:215px;width:470px;font-size:13px;line-height:20px;color:var(--ink)}
.about-text p+p{margin-top:20px}
.about .btn-outline{position:absolute;left:620px;top:450px}

/* expertise */
.expertise{top:1970px;height:1162px}
.exp-row{position:absolute;left:114px;width:980px}
.exp-photo{position:absolute;top:0}
.exp-body{position:absolute;font-size:12.5px;line-height:18px;color:var(--ink)}
.exp-body h3{font-size:15px;font-weight:700;margin-bottom:8px}
.exp-row.flip .exp-body{text-align:right}

/* quote */
.quote-band{top:3132px;height:263px;background:radial-gradient(ellipse at 50% 50%,#2d2b72 0%,var(--navy) 55%,var(--navy-deep) 100%);text-align:center;color:var(--white)}
.quote-mark{position:absolute;left:0;width:1200px;top:32px;font-family:"Libre Baskerville",Georgia,serif;font-size:60px;line-height:1}
.quote-text{position:absolute;left:0;width:1200px;top:108px;font-family:"Libre Baskerville",Georgia,serif;font-style:italic;font-weight:700;font-size:29px}
.quote-cite{position:absolute;left:0;width:1200px;top:158px;font-size:11px;color:#d8d8e6}

/* contact */
.contact{top:3395px;height:923px}
.contact-item{position:absolute;top:230px;display:flex;align-items:center;gap:12px}
.contact-icon{width:40px;height:40px;border-radius:50%;border:1px solid var(--navy);display:flex;align-items:center;justify-content:center}
.contact-label{font-size:10px;font-weight:700;letter-spacing:.5px;color:var(--ink)}
.contact-value{font-size:12.5px;color:var(--ink)}
.contact-panel{position:absolute;left:100px;top:300px;width:1000px;height:512px;background:var(--wash)}
.quote-form{position:absolute;left:14px;top:28px;width:471px}
.field-label{display:block;font-size:10px;font-weight:600;letter-spacing:.5px;color:var(--ink);margin-bottom:6px}
.field{height:36px;background:var(--field);margin-bottom:20px}
.field.tall{height:125px}
.submit{display:inline-flex;align-items:center;justify-content:center;gap:8px;width:172px;height:42px;background:var(--navy);color:var(--white);font-size:11px;font-weight:700;letter-spacing:1px;margin-top:8px}
.map{position:absolute;left:510px;top:0;width:490px;height:512px;background:linear-gradient(160deg,#eef0e8 0%,#e4e8dc 60%,#dfe4d6 100%)}
.ridge-mark{position:absolute;left:572px;top:884px;width:56px;height:56px;border-radius:50%;background:var(--white);border:2px solid var(--navy)}

/* footer */
.site-footer{top:4318px;height:297px;background:var(--footer);color:var(--white)}
.foot-col{position:absolute;top:80px;width:230px}
.foot-col h4{font-size:12px;font-weight:700;letter-spacing:1px;margin-bottom:16px}
.foot-col p,.foot-col li{font-size:11px;line-height:18px;color:#eeeeee;list-style:none}
.foot-col li::before{content:"› "}
.foot-line{display:flex;align-items:center;gap:8px;font-size:11px;font-weight:600;line-height:20px;white-space:nowrap}
.foot-btn{display:inline-flex;align-items:center;gap:6px;margin-top:8px;padding:0 14px;height:26px;background:var(--navy);font-size:10px;font-weight:700;letter-spacing:.5px}
.footer-bar{position:absolute;left:0;bottom:0;width:1200px;height:40px;background:var(--footer-bar);text-align:center;font-size:10px;line-height:40px;color:#e6e6e6}
</style>
</head>
<body>

<header class="section site-header">
  <div class="brand"><span class="brand-dot"></span><span class="brand-name">Copper Ridge Reserves</span></div>
  <div class="header-phone">
    <span class="phone-badge"><svg width="12" height="12" viewBox="0 0 24 24"><path fill="#fff" d="M6.6 10.8a15.1 15.1 0 0 0 6.6 6.6l2.2-2.2c.3-.3.7-.4 1-.2 1.1.4 2.3.6 3.6.6.6 0 1 .4 1 1V20c0 .6-.4 1-1 1A17 17 0 0 1 3 4c0-.6.4-1 1-1h3.5c.6 0 1 .4 1 1 0 1.3.2 2.5.6 3.6.1.3 0 .7-.2 1z"/></svg></span>
    208.555.0148
  </div>
  <nav class="main-nav">
    <span class="active">HOME</span><span>ABOUT US</span><span>RESERVE STUDIES ▾</span><span>CONTACT US</span>
  </nav>
</header>

<section class="section hero" role="img" aria-label="Photograph of an open desert highway stretching to the horizon at dusk">
  <div class="hero-copy">
    <h1 class="hero-title">YOUR FINANCIAL ROAD MAP</h1>
    <p class="hero-sub">for the Next 30 Years!</p>
    <div class="hero-actions">
      <span class="hero-btn secondary"><span class="tri"></span>LEARN MORE</span>
      <span class="hero-btn primary"><span class="tri"></span>REQUEST A QUOTE</span>
    </div>
  </div>
</section>

<section class="section services">
  <span class="rule-v" style="top:0;height:80px"></span>
  <h2 class="section-title" style="top:110px">WHAT WE DO</h2>

  <article class="service" style="left:108px">
    <svg class="service-icon" viewBox="0 0 150 150"><circle cx="75" cy="75" r="52" fill="none" stroke="#24215f" stroke-width="2"/><circle cx="75" cy="75" r="38" fill="#24215f"/><path d="M53 78 75 58l22 20h-6v18H59V78z" fill="#fff"/><rect x="70" y="84" width="10" height="12" fill="#24215f"/></svg>
    <h3 class="service-name">HOA &amp; Condominium Studies</h3>
    <p class="service-text">Every homeowners association is different. Different sets of assets, different financials and different historical backgrounds that have brought you to the present. Each of these is taken into consideration to customize your 30 year budget and build the most accurate, most precise long-term savings ("reserve") report you can buy.</p>
    <span class="btn-outline"><span class="tri"></span>LEARN MORE</span>
  </article>

  <article class="service" style="left:440px">
    <svg class="service-icon" viewBox="0 0 150 150"><circle cx="75" cy="75" r="52" fill="none" stroke="#24215f" stroke-width="2"/><circle cx="75" cy="75" r="38" fill="#24215f"/><rect x="58" y="56" width="34" height="42" fill="#fff"/><g fill="#24215f"><rect x="63" y="61" width="6" height="6"/><rect x="72" y="61" width="6" height="6"/><rect x="81" y="61" width="6" height="6"/><rect x="63" y="71" width="6" height="6"/><rect x="72" y="71" width="6" height="6"/><rect x="81" y="71" width="6" height="6"/><rect x="63" y="81" width="6" height="6"/><rect x="81" y="81" width="6" height="6"/><rect x="71" y="86" width="8" height="12"/></g></svg>
    <h3 class="service-name">Commercial, Vacation &amp; Time Share</h3>
    <p class="service-text">Your property represents a significant capital investment. In many cases, your business is dependent on the livelihood and functionality of the edifice in which it resides. We believe a fiscally sound plan and budget of capital expenses is as essential as the building itself. We are comprehensive, thorough and intense about our calculations.</p>
    <span class="btn-outline"><span class="tri"></span>LEARN MORE</span>
  </article>

  <article class="service" style="left:773px">
    <svg class="service-icon" viewBox="0 0 150 150"><circle cx="75" cy="75" r="52" fill="none" stroke="#24215f" stroke-width="2"/><circle cx="75" cy="75" r="38" fill="#24215f"/><path d="M75 52 88 74h-6l9 14H59l9-14h-6z" fill="#fff"/><rect x="72" y="88" width="6" height="10" fill="#fff"/><path d="M58 66 66 80h-4l6 10H48l6-10h-4z" fill="#fff"/><path d="M92 66l8 14h-4l6 10H82l6-10h-4z" fill="#fff"/></svg>
    <h3 class="service-name">Parks &amp; Public Lands</h3>
    <p class="service-text">Much like HOA's and condominiums, you have finite funds that originate from a constituent base of tax payers. Planning the use of these funds and repairs and/or maintenance of public assets is essential to transparency and candid communication with your constituents. Being in control of the future starts with a financial plan.</p>
    <span class="btn-outline"><span class="tri"></span>LEARN MORE</span>
  </article>
</section>

<section class="section about">
  <span class="rule-v" style="top:0;height:60px"></span>
  <h2 class="section-title" style="top:130px">WHO WE ARE</h2>
  <div class="about-video" role="img" aria-label="Video still of a dark night sky">
    <svg class="play" viewBox="0 0 52 52"><circle cx="26" cy="26" r="24" fill="none" stroke="#fff" stroke-width="2.5"/><path d="M21 15v22l17-11z" fill="#fff"/></svg>
  </div>
  <div class="about-text">
    <p>A fixed landmark on the horizon is a constant that travelers have relied on for centuries. Finding the way is simply knowing the right points of origin and following the map that the land has laid out before us.</p>
    <p>We love the open country! Amidst so much distance and a seemingly chaotic expanse of peaks, valleys and rivers, there is great order. Of all the detours and distractions along the road, a steady landmark remains ever true, ever vigilant and ever rooted. A financial plan should be equally so!</p>
  </div>
  <span class="btn-outline"><span class="tri"></span>LEARN MORE</span>
</section>

<section class="section expertise">
  <span class="rule-v" style="top:0;height:90px"></span>
  <h2 class="section-title" style="top:165px">BACKGROUND &amp; EXPERTISE</h2>

  <div class="exp-row" style="top:248px">
    <div class="exp-photo" role="img" aria-label="Photograph of financial papers, a calculator and eyeglasses on a desk" style="left:0;width:226px;height:138px;background:linear-gradient(135deg,#e9f1f7,#b9d3e6)"></div>
    <div class="exp-body" style="left:252px;top:6px;width:728px">
      <h3>Finances &amp; Balances</h3>
      <p>At the core, this is math. And as a science, strong conclusions founded in solid data yield a powerful planning tool. Not only math, however, as economic inputs have sway on the outcome of our projections. Moreover, construction and tradesmen are key to the ongoing costs and replacement values. We reach deep into your local market to ensure these variables are both accounted for and given their proper weight.</p>
    </div>
  </div>

  <div class="exp-row flip" style="top:448px">
    <div class="exp-body" style="left:0;top:6px;width:640px">
      <h3>The Finest Software</h3>
      <p>Our software is the only system that has been independently audited by a Certified Public Accounting firm. The results of the Quality Assurance Evaluation were that our system's functionality concept and logic, data input and output are operating in the manner intended and that no exceptions were found as a result of the attestation procedures. When it comes to a 30-year projection of income and expenses, we do not cut corners or hope for the best. We insist on being the best!</p>
    </div>
    <div class="exp-photo" role="img" aria-label="Photograph of a tablet showing blue bar charts" style="left:671px;width:308px;height:182px;background:linear-gradient(135deg,#f2f4f7,#c7d4e3)"></div>
  </div>

  <div class="exp-row" style="top:648px">
    <div class="exp-photo" role="img" aria-label="Photograph of a businessman in a suit working at a desk" style="left:0;width:308px;height:170px;background:linear-gradient(135deg,#f4f4f4,#b9bcc4)"></div>
    <div class="exp-body" style="left:333px;top:6px;width:647px">
      <h3>HOA &amp; State Expertise</h3>
      <p>In short, we read more than anyone we know. We read and keep tabs on the state statues that affect the HOA's, condominiums and commercial properties we serve. We know governing documents as they pertain to homeowners associations. Why? Because we read. We navigate these often confusing documents by diving in. Again and again. We often seek input and advice from other experts to ensure our course is set true. Our relationships with attorneys, property managers, legislators and tradesman are immensely important. Our reputation and yours count on it.</p>
    </div>
  </div>

  <div class="exp-row flip" style="top:840px">
    <div class="exp-body" style="left:0;top:6px;width:640px">
      <h3>Decades in Building</h3>
      <p>As a team, we have decades of experience in building and construction, estimating and financing reserves. Individually, our Reserve Analysts EACH have more than decade of experience with budgeting replacement costs and materials for reserve analytics.</p>
    </div>
    <div class="exp-photo" role="img" aria-label="Photograph of a team of colleagues joining hands outdoors" style="left:671px;width:308px;height:190px;background:linear-gradient(160deg,#cfdbe6,#5e6b7c)"></div>
  </div>
</section>

<section class="section quote-band">
  <div class="quote-mark">“</div>
  <p class="quote-text">If you fail to plan, you are planning to fail!</p>
  <p class="quote-cite">Elias Harlow</p>
</section>

<section class="section contact">
  <h2 class="section-title" style="top:110px">GET IN TOUCH</h2>

  <div class="contact-item" style="left:114px">
    <span class="contact-icon"><svg width="18" height="18" viewBox="0 0 24 24"><path fill="#24215f" d="M6.6 10.8a15.1 15.1 0 0 0 6.6 6.6l2.2-2.2c.3-.3.7-.4 1-.2 1.1.4 2.3.6 3.6.6.6 0 1 .4 1 1V20c0 .6-.4 1-1 1A17 17 0 0 1 3 4c0-.6.4-1 1-1h3.5c.6 0 1 .4 1 1 0 1.3.2 2.5.6 3.6.1.3 0 .7-.2 1z"/></svg></span>
    <div><div class="contact-label">PHONE</div><div class="contact-value">208.555.0148</div></div>
  </div>
  <div class="contact-item" style="left:440px">
    <span class="contact-icon"><svg width="18" height="18" viewBox="0 0 24 24"><rect x="3" y="6" width="18" height="13" fill="none" stroke="#24215f" stroke-width="2"/><path d="M3 6l9 7 9-7" fill="none" stroke="#24215f" stroke-width="2"/></svg></span>
    <div><div class="contact-label">EMAIL</div><div class="contact-value">hello@copperridgereserves.example</div></div>
  </div>
  <div class="contact-item" style="left:780px">
    <span class="contact-icon"><svg width="18" height="18" viewBox="0 0 24 24"><path fill="#24215f" d="M12 2a7 7 0 0 0-7 7c0 5 7 13 7 13s7-8 7-13a7 7 0 0 0-7-7zm0 9.5A2.5 2.5 0 1 1 12 6.5a2.5 2.5 0 0 1 0 5z"/></svg></span>
    <div><div class="contact-label">ADDRESS</div><div class="contact-value">418 N. 2100 E. Cedar Bluff ID 83507</div></div>
  </div>

  <div class="contact-panel">
    <form class="quote-form">
      <label class="field-label">NAME</label><div class="field"></div>
      <label class="field-label">EMAIL</label><div class="field"></div>
      <label class="field-label">PHONE</label><div class="field"></div>
      <label class="field-label">MESSAGE</label><div class="field tall"></div>
      <span class="submit"><span class="tri"></span>SUBMIT</span>
    </form>
    <div class="map" role="img" aria-label="Road map of the surrounding area with a pin marking the office"></div>
  </div>

  <span class="rule-v" style="top:822px;height:62px"></span>
  <span class="ridge-mark"></span>
</section>

<footer class="section site-footer">
  <div class="foot-col" style="left:114px">
    <h4>COMPANY</h4>
    <p>Copper Ridge Reserves, LLC expertise forecasting in top tier 30-year capital expense budgets for HOA's, condos, commercial properties and more! Plan now or pay later!</p>
  </div>
  <div class="foot-col" style="left:362px">
    <h4>SITEMAP</h4>
    <ul><li>Home</li><li>About Us</li><li>Reserve Studies</li><li>Contact Us</li></ul>
  </div>
  <div class="foot-col" style="left:614px">
    <h4>RESERVE STUDIES</h4>
    <ul><li>HOA Reserves</li><li>Condo Reserves</li><li>Hotels, Hospitality &amp; Commercial</li><li>Parks &amp; Public Lands</li></ul>
  </div>
  <div class="foot-col" style="left:866px">
    <h4>GET IN TOUCH</h4>
    <div class="foot-line">☎ 208.555.0148</div>
    <div class="foot-line">✉ hello@copperridgereserves.example</div>
    <div class="foot-line">⌖ 418 N. 2100 E. Cedar Bluff ID 83507</div>
    <span class="foot-btn"><span class="tri"></span>REQUEST A QUOTE</span>
  </div>
  <div class="footer-bar">©2019 Copper Ridge Reserves, LLC. All Rights Reserved</div>
</footer>

</body>
</html>
```